Larkfield Advisory Group LLC Business Card Design

I'm looking for a fresh, sharp, clean and current/modern format for my company. This is a start up in the professional services (security/risk management consulting) industry. Catering to C-suite executives as well as senior director types of halcyon 800 companies.

Target Market(s)

Halcyon 800 companies and their C-suite staff with particular focus on VP of Human Resources and Director of Security.

Industry/Entity Type

Business

Font styles to use
Serif

Colors
0455a3
9bcb3c
acd037
3377b5
eaf1f7

Requirements
Must have
• Fresh, sharp, clean and current/modern look and feel.

```html
<!DOCTYPE html>
<html lang="en">
<head>
<meta charset="utf-8">
<title>Larkfield Advisory Group LLC – Business Card</title>
<link rel="stylesheet" href="https://fonts.googleapis.com/css2?family=Source+Sans+3:wght@400;600;700&display=swap">
<style>
  :root {
    --brand-blue: #0455a3;
    --brand-navy: #1f3f8f;
    --brand-green: #9bcb3c;
    --brand-lime: #acd037;
    --brand-mid-blue: #3377b5;
    --brand-mist: #eaf1f7;
    --card-white: #fbfbfb;
    --text-grey: #5c5c5c;
    --text-dark: #222;
  }
  * { box-sizing: border-box; margin: 0; padding: 0; }
  html, body { width: 1200px; height: 900px; overflow: hidden; }
  body {
    background: var(--brand-mist);
    font-family: "Source Sans 3", "Helvetica Neue", Arial, sans-serif;
    position: relative;
  }
  .card {
    position: absolute;
    width: 720px;
    height: 411px;
    background: var(--card-white);
    border-radius: 4px;
    box-shadow: 0 10px 28px rgba(4, 85, 163, 0.16);
    overflow: hidden;
  }
  .card--front { left: 60px; top: 40px; }
  .card--back  { left: 420px; top: 470px; }

  .edge-band {
    position: absolute;
    left: 0; right: 0; bottom: 0;
    height: 28px;
    background: var(--brand-navy);
  }
  .edge-band__accent {
    position: absolute;
    right: 0; top: 0; bottom: 0;
    width: 110px;
    background: var(--brand-lime);
    border-top-left-radius: 14px;
  }

  .brand {
    position: absolute;
    display: flex;
    align-items: center;
    gap: 16px;
    white-space: nowrap;
  }
  .card--front .brand { right: 56px; top: 56px; }
  .card--back .brand { left: 50%; top: 50%; transform: translate(-50%, -62%); }
  .brand__dot {
    width: 58px; height: 58px;
    border-radius: 50%;
    background: var(--brand-blue);
    flex: none;
  }
  .brand__text { display: flex; flex-direction: column; }
  .brand__name {
    font-weight: 700;
    font-size: 30px;
    line-height: 1;
    color: var(--brand-blue);
    letter-spacing: 0.5px;
  }
  .brand__tagline {
    margin-top: 8px;
    display: flex;
    align-items: center;
    gap: 8px;
    font-weight: 600;
    font-size: 14px;
    letter-spacing: 2px;
    color: var(--brand-green);
  }
  .brand__tagline::before {
    content: "";
    width: 28px; height: 1px;
    background: var(--brand-green);
  }

  .holder {
    position: absolute;
    left: 50px; top: 168px;
  }
  .holder__name {
    font-weight: 700;
    font-size: 24px;
    color: var(--text-dark);
    line-height: 1.1;
  }
  .holder__role {
    font-size: 16px;
    color: var(--text-grey);
  }

  .contact-tab {
    position: absolute;
    left: 50px; bottom: 28px;
    width: 42px; height: 150px;
    background: var(--brand-mid-blue);
    border-radius: 10px 10px 0 0;
    display: flex;
    flex-direction: column;
    justify-content: space-evenly;
    align-items: center;
  }
  .contact-tab svg { width: 18px; height: 18px; }

  .contact-list {
    position: absolute;
    left: 108px; bottom: 28px;
    height: 150px;
    list-style: none;
    display: flex;
    flex-direction: column;
    justify-content: space-evenly;
    font-size: 15px;
    color: var(--text-grey);
  }
</style>
</head>
<body>

<section class="card card--front" aria-label="Business card front">
  <div class="brand">
    <span class="brand__dot"></span>
    <div class="brand__text">
      <span class="brand__name">Larkfield Advisory Group</span>
      <span class="brand__tagline">CLEAR, CALM &amp; SURE</span>
    </div>
  </div>

  <div class="holder">
    <p class="holder__name">Your Name</p>
    <p class="holder__role">Designation</p>
  </div>

  <div class="contact-tab" aria-hidden="true">
    <svg viewBox="0 0 20 20" fill="none" stroke="#fff" stroke-width="1.8"><rect x="5" y="2" width="10" height="16" rx="2"/><line x1="9" y1="15" x2="11" y2="15"/></svg>
    <svg viewBox="0 0 20 20" fill="#fff"><path d="M10 1a6 6 0 0 0-6 6c0 4.5 6 12 6 12s6-7.5 6-12a6 6 0 0 0-6-6zm0 8.3A2.3 2.3 0 1 1 10 4.7a2.3 2.3 0 0 1 0 4.6z"/></svg>
    <svg viewBox="0 0 20 20" fill="none" stroke="#fff" stroke-width="1.8"><rect x="2" y="4" width="16" height="12" rx="1"/><polyline points="2,5 10,11 18,5"/></svg>
    <svg viewBox="0 0 20 20" fill="none" stroke="#fff" stroke-width="1.6"><circle cx="10" cy="10" r="8"/><ellipse cx="10" cy="10" rx="3.5" ry="8"/><line x1="2" y1="10" x2="18" y2="10"/></svg>
  </div>

  <ul class="contact-list">
    <li>(+123) - 456 - 7890</li>
    <li>Your Complete Address Here</li>
    <li>info@larkfieldadvisory.com</li>
    <li>www.larkfieldadvisory.com</li>
  </ul>

  <div class="edge-band"><span class="edge-band__accent"></span></div>
</section>

<section class="card card--back" aria-label="Business card back">
  <div class="brand">
    <span class="brand__dot"></span>
    <div class="brand__text">
      <span class="brand__name">Larkfield Advisory Group</span>
      <span class="brand__tagline">CLEAR, CALM &amp; SURE</span>
    </div>
  </div>
  <div class="edge-band"><span class="edge-band__accent"></span></div>
</section>

</body>
</html>
```